Book cover Design for her new book called 'Walking a path lined with courage and grace'

My name is Velorashi, I am the founder of The Quiet Lantern.
http://velorashi-wren.examplestore.com/
My book is an inspirational story of love and triumphing from adversity. After 40 years of surviving a life full of sexual abuse, physical and mental abuse and living with the effects of poor self-esteem and post traumatic stress disorder, this book is a guide to help others navigate away from negative emotions and help them find their own light in life. With the techniques developed and described in the book The Quiet Lantern's mission is to empower people with the journey to their own hearts and create warmth, love and inspiration.
The colours in the website represent the softness that I love and I prefer flowers. The colour also can be soft as well as vibrant and feminine. The final design should represent healing, love, inspiration and passion.

Target Market(s)

Women over the age of 25 -80
Teenagers suffering from depression
Men and women suffering from poor self esteem
Woman who have poor self confidence.

Requirements
Should not have
• Should not be dark in colour or imagery.

```html
<!DOCTYPE html>
<html lang="en">
<head>
<meta charset="UTF-8">
<title>Walking a Path Lined with Courage and Grace — Book Cover</title>
<link href="https://fonts.googleapis.com/css2?family=Cinzel:wght@400;600&family=Parisienne&family=Cormorant+SC:wght@500&display=swap" rel="stylesheet">
<style>
  :root {
    --page-bg: #ffffff;
    --sky-top: #e9c6ea;
    --sky-mid: #f3d9ec;
    --haze: #dcb6c9;
    --field-far: #a8884a;
    --field-mid: #c79a2c;
    --field-near: #6b4a1c;
    --ink-dark: #2a2a2a;
    --ink-teal: #1f4b50;
    --ink-light: #fbf3e2;
  }
  * { margin: 0; padding: 0; box-sizing: border-box; }
  html, body {
    width: 1200px;
    height: 900px;
    overflow: hidden;
    background: var(--page-bg);
  }
  .canvas {
    width: 1200px;
    height: 900px;
    display: flex;
    align-items: center;
    justify-content: center;
  }
  .book-cover {
    position: relative;
    width: 560px;
    height: 840px;
    overflow: hidden;
    box-shadow: 0 10px 30px rgba(0, 0, 0, 0.18);
  }
  .cover-scene {
    position: absolute;
    inset: 0;
    background: linear-gradient(to bottom,
      var(--sky-top) 0%,
      var(--sky-mid) 30%,
      var(--haze) 46%,
      var(--field-far) 52%,
      var(--field-mid) 68%,
      var(--field-near) 100%);
  }
  .title-block {
    position: absolute;
    top: 62px;
    left: 0;
    right: 0;
    text-align: center;
  }
  .title-lead {
    font-family: "Cinzel", serif;
    font-weight: 400;
    font-size: 27px;
    letter-spacing: 1px;
    color: var(--ink-dark);
  }
  .title-main {
    font-family: "Parisienne", cursive;
    font-weight: 400;
    color: var(--ink-teal);
    line-height: 1;
  }
  .title-main .word-large {
    display: block;
    font-size: 124px;
    margin-top: 18px;
  }
  .title-main .word-small {
    display: block;
    font-size: 100px;
    margin-top: -8px;
  }
  .title-main .joiner {
    font-size: 56px;
    vertical-align: middle;
    margin-right: 6px;
  }
  .author-block {
    position: absolute;
    bottom: 48px;
    left: 0;
    right: 0;
    text-align: center;
    color: var(--ink-light);
  }
  .author-name {
    font-family: "Cinzel", serif;
    font-weight: 600;
    font-size: 44px;
    letter-spacing: 3px;
  }
  .author-role {
    font-family: "Cormorant SC", serif;
    font-weight: 500;
    font-size: 22px;
    margin-top: -2px;
  }
</style>
</head>
<body>
  <main class="canvas">
    <section class="book-cover">
      <div class="cover-scene" role="img" aria-label="Photograph of a wide sunflower field under a soft pink sky with sun rays"></div>
      <header class="title-block">
        <p class="title-lead">Walking a Path Lined with</p>
        <h1 class="title-main">
          <span class="word-large">Courage</span>
          <span class="word-small"><span class="joiner">and</span>Grace</span>
        </h1>
      </header>
      <footer class="author-block">
        <p class="author-name">Velorashi</p>
        <p class="author-role">Founder of The Quiet Lantern</p>
      </footer>
    </section>
  </main>
</body>
</html>
```